Business Card Needed for Crafter of Pottery, Jewelry and Artwork

Calling all designers in search of an artistic challenge.

I need a new business card design for my pottery, jewelry and artwork business, Woven Glass and Tide, based in Vancouver BC.

I would like a card that is bright and inviting and preferably incorporates my logo and a sample of photos of my work while having a clean fresh look. The following contact details would preferably be included on the card as well:
• Helena Pikeworth
• Designer
• Phone: 604.555.0172
• Email: Designer@WovenGlassandTide.example
• Website: www.WovenGlassandTide.example
• Blog: www.ShapingHillside.example

The logo is attached in two color schemes in both Vector and Source formats. On past cards I’ve also included photos of my work. By including photos of the work the pieces are showcased and it catches people’s eye and prompts them to pick up the card and look at it more closely. For example, if I leave a stack in a coffee shop I want people to be drawn to the card, to pick it up and get a sense of the my product lines. Please feel free to pull photos of my work directly off of my website. If you need photos with higher pixels please let me know and I’ll email them directly to you. The website background is bffbda (191, 251, 218). I would like the business cards to match the feel of the website for consistency but the cards do not need to use the exact same colors. My website and current business card are predominantly turquoise shades. The background uses stripes provided by the website template. I don’t know the exact colors of the stripes.

My current business card is attached to show the use of photos in a design. Please note that I am not thrilled with my own design and am looking for variations and completely new designs. This example is not meant to be used as a template or starting point.

Here is some background surrounding my company:
WGT offers one of a kind jewelry, pottery, artwork and leather bags each designed with a twist. The pottery varies from rustic every day functional ware to raku artwork. The jewelry ranges from simple sterling every day pieces to multimedia pieces incorporating stone, metal, ceramics and fabric. The artwork is multimedia, typically acrylic paired with a natural element such as bark. All the bags are leather with reworked kimono fabric or patterned silk lining.

Feel free to check out my website to get a flavour for my work and the color scheme I've used on marketing materials so far. www.wovenglassandtide.example
Updates

Thank you to everyone who has submitted a design so far. I hope everyone has received some helpful feedback.

I'm going to post a survey to customers and friends asking for their votes. If you have new designs to submit please try to get them in by Saturday March 30 at noon so that I can include it in the survey launch.

Thank you

Target Market(s)

Females aged 25-65 interested in one of a kind functional pottery and jewelry.

Industry/Entity Type

Coffee Shop

Requirements
Must have
• Contact information, website, blog
Nice to have
• Logo, photos

```html
<!DOCTYPE html>
<html lang="en">
<head>
<meta charset="utf-8">
<title>Woven Glass and Tide – Business Card</title>
<link rel="stylesheet" href="https://fonts.googleapis.com/css2?family=Libre+Baskerville:wght@400;700&display=swap">
<style>
  :root {
    --page: #e8e6e1;
    --card: #cfe9c6;
    --teal: #27a397;
    --navy: #2d2f6a;
    --cream: #fbf6cf;
    --white: #ffffff;
    --logo-fill: #1fb7a8;
  }
  * { margin: 0; padding: 0; box-sizing: border-box; }
  html, body { width: 1200px; height: 741px; overflow: hidden; }
  body {
    background: var(--page);
    font-family: "Libre Baskerville", "Book Antiqua", Georgia, serif;
    color: var(--navy);
    position: relative;
  }
  .card {
    position: absolute;
    left: 254px;
    width: 714px;
    background: var(--card);
    overflow: hidden;
  }
  .card--front { top: 24px; height: 327px; }
  .card--back { top: 381px; height: 330px; }

  .rule {
    position: absolute;
    left: 0; right: 0;
    height: 3px;
    background: var(--teal);
  }

  /* Front */
  .brand-title {
    position: absolute;
    top: 24px; left: 0; right: 0;
    text-align: center;
    font-size: 30px;
    font-weight: 700;
  }
  .gallery-band {
    position: absolute;
    top: 90px; left: 0; right: 0;
    height: 140px;
    background: var(--cream);
  }
  .gallery-panel {
    position: absolute;
    top: 0; bottom: 0;
    left: 63px; width: 587px;
    background: var(--white);
  }
  .gallery-photo {
    position: absolute;
    top: 26px; height: 114px;
  }
  .photo-raku {
    left: 29px; width: 227px;
    background: linear-gradient(160deg, #c9c4c0 0%, #7b5a5e 45%, #5c6f7e 70%, #d2a87a 100%);
  }
  .photo-cup {
    left: 257px; width: 113px;
    background: linear-gradient(180deg, #6a4a2e 0%, #8a5a32 40%, #4f9a7c 70%, #86c7aa 100%);
  }
  .photo-mugs {
    left: 371px; width: 185px;
    background: linear-gradient(180deg, #f4f6f6 0%, #9ccfd0 45%, #5d8f93 75%, #3f4a4f 100%);
  }
  .front-url {
    position: absolute;
    top: 253px; left: 0; right: 0;
    text-align: center;
    font-size: 20px;
    font-weight: 700;
  }

  /* Back */
  .holder-name {
    position: absolute;
    top: 38px; left: 63px;
    font-size: 33px;
    font-weight: 700;
  }
  .holder-role {
    position: absolute;
    top: 82px; left: 67px;
    font-size: 17px;
  }
  .contact-list {
    position: absolute;
    top: 221px; left: 43px;
    list-style: none;
    font-size: 13px;
    line-height: 16.5px;
    white-space: nowrap;
  }
  .contact-list li::before {
    content: "•";
    display: inline-block;
    width: 20px;
    text-align: left;
  }
  .brand-mark {
    position: absolute;
    left: 361px; top: 47px;
    width: 310px; height: 232px;
    border-radius: 50%;
    background: var(--logo-fill);
    border: 5px solid var(--white);
    display: flex;
    align-items: center;
    justify-content: center;
    text-align: center;
  }
  .brand-mark span {
    font-size: 22px;
    font-weight: 700;
    color: var(--navy);
    line-height: 1.3;
  }
</style>
</head>
<body>
  <section class="card card--front">
    <h1 class="brand-title">Woven Glass and Tide</h1>
    <div class="rule" style="top:58px"></div>
    <div class="gallery-band">
      <div class="gallery-panel">
        <div class="gallery-photo photo-raku" role="img" aria-label="Photo of raku pottery bowls and small jewellery pieces"></div>
        <div class="gallery-photo photo-cup" role="img" aria-label="Photo of a glazed cup with brown drips over green"></div>
        <div class="gallery-photo photo-mugs" role="img" aria-label="Photo of three turquoise glazed mugs"></div>
      </div>
    </div>
    <p class="front-url">www.WovenGlassandTide.example</p>
    <div class="rule" style="top:290px"></div>
  </section>

  <section class="card card--back">
    <h2 class="holder-name">Helena Pikeworth</h2>
    <p class="holder-role">Designer</p>
    <div class="rule" style="top:106px"></div>
    <div class="brand-mark"><span>Woven Glass<br>and Tide</span></div>
    <ul class="contact-list">
      <li>Phone: 604.555.0172</li>
      <li>Email: Designer@WovenGlassandTide.example</li>
      <li>Website: www.WovenGlassandTide.example</li>
      <li>Blog: www.ShapingHillside.example</li>
    </ul>
    <div class="rule" style="top:296px"></div>
  </section>
</body>
</html>
```